High Quality Hemp Flowers Packaging Design

We need a logo and packaging design for a new CBD hemp product. We sell CBD rich hemp flower- tops to our customers in Europe. CBD's natural benefits are extensive and generally used for all sorts of reasons.
Our strains are of the highest quality and used as an aromatic product. Thus the design should look clean and modern with a slight organic touch. We'd like people to associate our product with a luxury product like a good wine or whiskey but still being modern, healthy and organic.
The product comes in a brown cardboard paper tube and the design needs to include:
-our logo made of the "vesko amulett" (attachment 1 vesko amulett)
-our website: "tobrinu.eu"
-the product name: "vesko"
tube properties:
tube size: 6cm diameter, 7cm height (please see attachment 2 Paper Tube 6cm diameter, 7cm height. jpg)
• material: 2mm thickness cardboard+brown kraft paper (like in attachment 3 Paper Tube colour.jpg – picture just a sample for the material – size is not correctly displayed in this picture)
• coated aluminum foil paper inside
• colour/ product name: whatever colour and where ever you want to place it in your design
• colour/ vesko amulet logo: whatever colour and where ever you want to place it in your design
• sticker (2-2.5 x 5-6,5cm –> whatever the designer thinks works better) for sealing use, to keep the two parts of the tube together and it needs to have a placeholder for the date of the packaging (like in attachment 2 Paper Tube 6cm diameter 7cm height – but the sticker will not cover the full side of the tube as in attachment 2, but just 5-6.5 cm)
• “inner” tube could be color printing (for clarification which part please see attachment 3 Paper Tube colour.jpg -> the white part – picture just a sample for the “white part” – size is not correctly displayed in this picture
- We dont need any marihuana leafs or signs.

```html
<!DOCTYPE html>
<html lang="en">
<head>
<meta charset="utf-8">
<title>Vesko – tube label</title>
<link rel="stylesheet" href="https://fonts.googleapis.com/css2?family=EB+Garamond:wght@400&display=swap">
<style>
  :root {
    --page: #e8e5e1;
    --paper: #ffffff;
    --ink: #111111;
    --wash-top: #eef3e8;
    --wash-mid: #f5f6e6;
    --wash-bottom: #eaf0e0;
  }
  * { box-sizing: border-box; margin: 0; padding: 0; }
  html, body {
    width: 1200px;
    height: 1149px;
    overflow: hidden;
    background: var(--page);
  }
  .canvas {
    position: relative;
    width: 1200px;
    height: 1149px;
  }
  .label {
    position: absolute;
    left: 396px;
    top: 49px;
    width: 408px;
    height: 1050px;
    background: var(--paper);
    overflow: hidden;
  }
  .label__wash {
    position: absolute;
    inset: 0;
    background: linear-gradient(180deg, var(--wash-top) 0%, var(--wash-mid) 50%, var(--wash-bottom) 100%);
  }
  .title-panel {
    position: absolute;
    left: 48px;
    top: 398px;
    width: 328px;
    height: 390px;
    background: var(--paper);
    border: 7px solid var(--ink);
    padding: 9px;
  }
  .title-panel__inner {
    position: relative;
    width: 100%;
    height: 100%;
    border: 2px solid var(--ink);
    font-family: "EB Garamond", Garamond, serif;
    font-weight: 400;
    color: var(--ink);
    text-align: center;
  }
  .brand-mark {
    position: absolute;
    left: 0;
    right: 0;
    top: 58px;
    display: flex;
    justify-content: center;
    align-items: center;
    gap: 8px;
    font-size: 20px;
    line-height: 1;
  }
  .brand-mark__dot {
    width: 14px;
    height: 14px;
    border-radius: 50%;
    background: var(--ink);
  }
  .product-name {
    position: absolute;
    left: 0;
    right: 0;
    top: 152px;
    font-size: 44px;
    font-weight: 400;
    letter-spacing: 0.03em;
    line-height: 1;
  }
  .website {
    position: absolute;
    left: 0;
    right: 0;
    top: 292px;
    font-size: 26px;
    line-height: 1;
  }
  .date-field {
    position: absolute;
    left: 104px;
    top: 923px;
    width: 195px;
    height: 56px;
    background: var(--paper);
  }
</style>
</head>
<body>
  <main class="canvas">
    <section class="label">
      <div class="label__wash" role="img" aria-label="Pastel green and cream watercolour brush-stroke pattern"></div>
      <div class="title-panel">
        <div class="title-panel__inner">
          <div class="brand-mark"><span class="brand-mark__dot"></span><span>vesko</span></div>
          <h1 class="product-name">VESKO</h1>
          <p class="website">tobrinu.eu</p>
        </div>
      </div>
      <div class="date-field"></div>
    </section>
  </main>
</body>
</html>
```